Software engineering company needs business card

I need a cool business card. Company: Byte Merano Larchwood Ave 41 58213 Dunmere Name: Gerald Hofmann CEO / Managing Director & Owner

Industry/Entity Type

Business

```html
<!DOCTYPE html>
<html lang="de">
<head>
<meta charset="utf-8">
<title>Byte Merano – Visitenkarte</title>
<link rel="stylesheet" href="https://fonts.googleapis.com/css2?family=Arimo:wght@400;700&display=swap">
<style>
  :root {
    --backdrop: #d3d4d5;
    --card: #ececec;
    --brand-green: #a5c44d;
    --brand-grey: #5c5c5c;
    --ink: #262626;
    --paper-white: #f7f7f7;
  }
  * { box-sizing: border-box; margin: 0; padding: 0; }
  html, body { width: 1200px; height: 710px; overflow: hidden; }
  body {
    background: var(--backdrop);
    font-family: "Arimo", Arial, sans-serif;
    position: relative;
  }
  .card {
    position: absolute;
    top: 185px;
    width: 560px;
    height: 340px;
    background: var(--card);
    overflow: hidden;
    box-shadow: 0 10px 24px rgba(0,0,0,0.18);
  }
  .card--front { left: 30px; }
  .card--back { left: 610px; }

  .brand {
    display: flex;
    align-items: center;
    gap: 14px;
    color: var(--brand-grey);
    font-weight: 400;
    letter-spacing: 3px;
    text-transform: uppercase;
  }
  .brand__square {
    width: 34px;
    height: 34px;
    background: var(--brand-green);
    flex: none;
  }
  .card--front .brand {
    position: absolute;
    left: 24px;
    top: 58px;
    font-size: 34px;
  }
  .card--back .brand {
    position: absolute;
    left: 0;
    right: 0;
    top: 146px;
    justify-content: center;
    font-size: 36px;
  }

  .wave { position: absolute; inset: 0; width: 100%; height: 100%; }
  .wave__green { fill: var(--brand-green); }
  .wave__swoosh { fill: var(--brand-grey); }

  .person {
    position: absolute;
    left: 20px;
    top: 238px;
  }
  .person__name {
    color: var(--paper-white);
    font-size: 24px;
    font-weight: 700;
    letter-spacing: -0.2px;
  }
  .person__role {
    margin-top: 4px;
    color: var(--ink);
    font-size: 13px;
  }
  .divider {
    position: absolute;
    left: 232px;
    top: 248px;
    width: 2px;
    height: 82px;
    background: var(--paper-white);
  }
  .address {
    position: absolute;
    right: 22px;
    bottom: 20px;
    color: var(--ink);
    font-size: 15px;
  }
</style>
</head>
<body>
  <section class="card card--front" aria-label="Vorderseite">
    <svg class="wave" viewBox="0 0 560 340" aria-hidden="true">
      <path class="wave__swoosh" d="M230,166 C340,200 450,196 560,146 L560,178 C470,212 360,214 230,166 Z"/>
      <path class="wave__green" d="M0,195 C110,145 220,170 320,198 C420,224 500,220 560,198 L560,340 L0,340 Z"/>
    </svg>
    <div class="brand"><span class="brand__square"></span>Byte Merano</div>
    <div class="person">
      <p class="person__name">Gerald Hofmann</p>
      <p class="person__role">CEO / Geschäftsführer &amp; Inhaber</p>
    </div>
    <div class="divider"></div>
    <p class="address">Larchwood Ave 41 58213 Dunmere</p>
  </section>

  <section class="card card--back" aria-label="Rückseite">
    <div class="brand"><span class="brand__square"></span>Byte Merano</div>
  </section>
</body>
</html>
```